ZEH Project Signage

Need a sign to be displayed in the front of properties currently under Construction or Renovation to advertise our company information. Need it to be Professional and Contemporary. We are a Design/Build Construction Company. Information should include Company Name, email, website, phone number. Attached: Logo and company brochure, also included and inspiration images

```html
<!DOCTYPE html>
<html lang="en">
<head>
<meta charset="utf-8">
<title>ZEH Construction – Project Sign</title>
<link rel="stylesheet" href="https://fonts.googleapis.com/css2?family=Montserrat:wght@500;600;700;800&display=swap">
<style>
  :root {
    --backdrop: #232323;
    --sign-white: #ffffff;
    --sign-black: #161616;
    --ink: #111111;
    --accent: #f2ea40;
    --text-light: #ffffff;
  }
  * { margin: 0; padding: 0; box-sizing: border-box; }
  html, body { width: 1200px; height: 1200px; overflow: hidden; background: var(--backdrop); }
  body { font-family: "Montserrat", sans-serif; position: relative; }

  .sign {
    position: absolute; left: 250px; top: 75px;
    width: 700px; height: 1049px;
    background: var(--sign-black);
    overflow: hidden;
  }
  .brand-panel {
    position: absolute; left: 0; top: 0; width: 700px; height: 492px;
    background: var(--sign-white);
  }
  .brand-name {
    position: absolute; left: 0; width: 700px; top: 180px;
    text-align: center; font-weight: 600; font-size: 52px;
    letter-spacing: 3px; color: var(--ink); line-height: 1; white-space: nowrap;
  }
  .brand-rule {
    position: absolute; left: 38px; top: 249px; width: 624px; height: 5px;
    background: var(--accent); border-radius: 3px;
  }
  .brand-tagline {
    position: absolute; left: 0; width: 700px; top: 265px;
    text-align: center; font-weight: 600; font-size: 27px;
    letter-spacing: 3px; color: var(--ink); line-height: 1; white-space: nowrap;
  }

  .contact-panel { position: absolute; left: 0; top: 492px; width: 700px; height: 557px; }
  .icon { position: absolute; width: 45px; height: 45px; }
  .icon-pin { left: 34px; top: 30px; }
  .icon-mail { left: 34px; top: 430px; }
  .icon-web { left: 42px; top: 485px; }

  .address {
    position: absolute; left: 68px; width: 600px; top: 29px;
    text-align: center; color: var(--text-light);
    font-weight: 600; font-size: 38px; line-height: 42px; letter-spacing: -0.8px;
    white-space: nowrap;
  }
  .label {
    position: absolute; left: 267px; width: 167px; height: 48px;
    border: 2px solid var(--accent); border-radius: 6px; background: #000;
    color: var(--accent); font-weight: 700; font-size: 32px;
    text-align: center; line-height: 44px; letter-spacing: -0.5px;
  }
  .label-direct { top: 143px; }
  .label-office { top: 279px; }
  .phone {
    position: absolute; left: 0; width: 700px; text-align: center;
    color: var(--accent); font-weight: 800; font-size: 74px;
    line-height: 1; letter-spacing: -1px; white-space: nowrap;
  }
  .phone-direct { top: 191px; }
  .phone-office { top: 328px; }
  .email, .website {
    position: absolute; left: 84px; width: 590px; color: var(--text-light);
    line-height: 1; letter-spacing: -0.5px; text-align: center; white-space: nowrap;
  }
  .email { top: 428px; font-size: 40px; font-weight: 500; }
  .website { top: 484px; font-size: 39px; font-weight: 700; }
  .website .domain { color: var(--accent); }
</style>
</head>
<body>
  <div class="sign">
    <section class="brand-panel">
      <div class="brand-name">ZEH CONSTRUCTION</div>
      <div class="brand-rule"></div>
      <div class="brand-tagline">LUXURY RENOVATIONS</div>
    </section>

    <section class="contact-panel">
      <svg class="icon icon-pin" viewBox="0 0 46 46" aria-hidden="true">
        <circle cx="23" cy="23" r="21.5" fill="#000" stroke="#f2ea40" stroke-width="2"/>
        <path d="M23 11a7 7 0 0 0-7 7c0 5.5 7 12 7 12s7-6.5 7-12a7 7 0 0 0-7-7z" fill="#f2ea40"/>
        <circle cx="23" cy="18" r="2.6" fill="#000"/>
        <ellipse cx="23" cy="33" rx="9" ry="3" fill="none" stroke="#f2ea40" stroke-width="1.6"/>
      </svg>
      <p class="address">1450 NW 4TH AVE., STE. 310<br>CORAL BAY, FL 33480</p>

      <div class="label label-direct">DIRECT</div>
      <p class="phone phone-direct">555.302.4817</p>

      <div class="label label-office">OFFICE</div>
      <p class="phone phone-office">555.302.6290</p>

      <svg class="icon icon-mail" viewBox="0 0 46 46" aria-hidden="true">
        <circle cx="23" cy="23" r="21.5" fill="#000" stroke="#f2ea40" stroke-width="2"/>
        <rect x="12" y="16" width="22" height="15" rx="1.5" fill="#f2ea40"/>
        <path d="M12 17l11 8 11-8" fill="none" stroke="#000" stroke-width="1.8"/>
      </svg>
      <p class="email">dario@zehconstruction.com</p>

      <svg class="icon icon-web" viewBox="0 0 46 46" aria-hidden="true">
        <circle cx="23" cy="23" r="21.5" fill="#000" stroke="#f2ea40" stroke-width="2"/>
        <g fill="none" stroke="#f2ea40" stroke-width="1.6">
          <circle cx="23" cy="23" r="10"/>
          <ellipse cx="23" cy="23" rx="4.5" ry="10"/>
          <path d="M13 23h20M15 17.5h16M15 28.5h16"/>
        </g>
      </svg>
      <p class="website">www.<span class="domain">zehconstruction</span>.com</p>
    </section>
  </div>
</body>
</html>
```